New women's health clinic needs a new home!!

We need a professional website for our modern women's health clinic. Needs to be in wordpress. Back end needs to be accesible by novice admin staff. Text and stock photography supplied by us. We need approximately 5 pages with 3-4 subpages each. Links to social media a must. Blog a must. Patients will need to be able to download e-books after supplying an e-mail address. Mobile-friendly is a must!

We created our logo through this site. Please refer to the logo for style themes.

Target Market(s)

Women aged 28-55

Industry/Entity Type

Health

Coding

Coded - Design and coding required

Number of Pages Required

5+ page

Font styles to use
Sans Serif

Colors
886aae
cee9f5
3377b5
d3a5cc
ffffff
eddcec
6e479c
85abd2
876aae

Requirements
Must have
• Wordpress
• Social media ready
• Mobile-friendly to Plinexa's specs
• Ability to download e-books
• Captures data on back end

```html
<!DOCTYPE html>
<html lang="en">
<head>
<meta charset="utf-8">
<title>Solvane Women's Health</title>
<link href="https://fonts.googleapis.com/css2?family=Open+Sans:ital,wght@0,400;0,600;0,700;1,400&family=Lora:ital@1&display=swap" rel="stylesheet">
<style>
:root{
  --purple:#6e479c;
  --purple-mid:#886aae;
  --pink:#d3a5cc;
  --lilac:#eddcec;
  --sky:#cee9f5;
  --blue:#3377b5;
  --blue-soft:#85abd2;
  --ink:#4a4a55;
  --muted:#8a8a96;
  --dark:#2c2d33;
  --darker:#1f2024;
  --white:#ffffff;
  --page:#f3f1f6;
}
*{margin:0;padding:0;box-sizing:border-box}
html,body{width:700px;height:1200px;overflow:hidden}
body{font-family:"Open Sans",Arial,sans-serif;background:var(--page);color:var(--ink);position:relative;font-size:9px;line-height:1.45}
.abs{position:absolute}

/* header */
.site-header{left:0;top:0;width:700px;height:56px;background:var(--white)}
.brand{left:47px;top:12px;display:flex;align-items:center;gap:7px}
.brand-dot{width:30px;height:30px;border-radius:50%;background:var(--lilac)}
.brand-name{color:var(--purple);font-weight:700;font-size:10px;line-height:1.2;letter-spacing:.5px}
.search{left:228px;top:20px;width:110px;height:18px;border:1px solid #d8d6de;border-radius:2px;font-size:8px;color:var(--muted);padding:3px 6px}
.contact{top:14px;display:flex;align-items:center;gap:6px;font-size:8px;line-height:1.3}
.contact .ico{width:22px;height:22px;border-radius:50%;background:var(--purple-mid);display:flex;align-items:center;justify-content:center}
.contact strong{display:block;color:var(--muted);font-weight:400}
.contact span{color:var(--ink);font-weight:600}

/* nav */
.main-nav{left:0;top:56px;width:700px;height:26px;background:var(--lilac);border-top:1px solid #ddd0e4}
.main-nav ul{list-style:none;display:flex;margin-left:47px;width:610px;height:100%}
.main-nav li{flex:1;text-align:center;font-size:7.5px;font-weight:600;color:var(--purple);line-height:26px;letter-spacing:.3px}
.main-nav li.active{background:var(--white)}

/* hero */
.hero{left:0;top:82px;width:700px;height:280px;background:linear-gradient(90deg,#8e9ea9 0%,#a9b7c1 45%,#c6d0d7 100%)}
.hero-photo{left:360px;top:0;width:340px;height:280px;background:linear-gradient(180deg,#b9c5cc 0%,#9cb1bd 55%,#6f8fa6 100%)}
.hero-copy{left:62px;top:48px;width:290px;color:var(--white)}
.hero-kicker{font-size:30px;font-weight:700;letter-spacing:1px;line-height:1}
.hero-title{font-family:"Lora",Georgia,serif;font-style:italic;font-size:38px;line-height:1.15;margin-bottom:8px}
.hero-lead{font-size:14px;line-height:1.35;color:#eef2f5}
.btn{display:inline-block;background:var(--purple);color:var(--white);font-weight:600;border-radius:2px;text-align:center}
.hero .btn{margin-top:16px;font-size:9px;padding:8px 16px}

/* ebook bar */
.ebook-bar{left:0;top:362px;width:700px;height:60px;background:var(--dark)}
.ebook-copy{left:62px;top:12px;width:230px;color:var(--white)}
.ebook-copy h3{font-size:11px;font-weight:600;margin-bottom:2px}
.ebook-copy p{font-size:7px;color:#aeb0b8}
.ebook-bar .btn{left:345px;top:17px;font-size:8px;padding:7px 14px;background:var(--pink);color:var(--purple)}

/* main column */
.content{left:47px;top:432px;width:432px}
.section-title{color:var(--purple);font-size:13px;font-weight:600;margin-bottom:6px}
.about{height:170px;position:relative}
.about p{width:250px;font-size:7.5px;color:var(--muted);margin-bottom:6px}
.about .btn{font-size:8px;padding:6px 12px;margin-top:4px}
.about-photo{position:absolute;right:0;top:18px;width:160px;height:135px;background:linear-gradient(180deg,#bfd9ef 0%,#d9e8f3 55%,#a9c48b 100%)}
.tips{margin-top:14px}
.tips-grid{display:grid;grid-template-columns:repeat(4,1fr);gap:12px 12px}
.tip .thumb{height:72px;margin-bottom:5px}
.tip h4{font-size:8px;font-weight:600;color:var(--ink)}
.tip p{font-size:7px;color:var(--muted)}
.t1{background:linear-gradient(135deg,#e5dccf,#c7b49e)}
.t2{background:linear-gradient(135deg,#d9d4d0,#9f8b82)}
.t3{background:linear-gradient(135deg,#8b5a3c,#d6b39a)}
.t4{background:linear-gradient(135deg,#f0e6e0,#c9b3a7)}
.t5{background:linear-gradient(135deg,#dfe9ee,#a9bfcc)}
.t6{background:linear-gradient(135deg,#bcd7ea,#5d8fb8)}
.t7{background:linear-gradient(135deg,#c2d9e8,#e9e2d6)}
.t8{background:linear-gradient(135deg,#ece3dc,#b99b88)}
.tips .btn{float:right;margin-top:12px;font-size:8px;padding:6px 14px}

/* sidebar */
.sidebar{left:497px;top:372px;width:161px}
.card{background:var(--white);margin-bottom:10px}
.card-head{background:var(--purple-mid);color:var(--white);font-size:10px;font-weight:600;padding:8px 10px}
.card-body{padding:8px 10px;font-size:7px;color:var(--muted)}
.field{height:17px;border:1px solid #ddd8e3;margin-top:6px;font-size:7px;padding:3px 5px;color:#aaa}
.card .btn{font-size:8px;padding:6px 0;width:100%;margin-top:8px}
.story-photo{height:80px;background:linear-gradient(135deg,#e8d9e6 0%,#c7a6c3 100%)}
.card h5{color:var(--purple);font-size:10px;font-weight:600;margin-bottom:3px}
.testimonial{text-align:center}
.testimonial h5{font-style:italic;font-weight:400;font-size:13px;margin:2px 0 6px}
.avatar{width:62px;height:62px;border-radius:50%;margin:0 auto 6px;background:linear-gradient(135deg,#f3e3c8,#d9b98b)}
.testimonial .name{color:var(--purple);font-weight:600;font-size:8px}
.testimonial .role{color:var(--ink);font-size:7px;margin-bottom:4px}

/* footer */
.site-footer{left:0;top:970px;width:700px;height:196px;background:var(--dark);color:#b8b9c1}
.footer-cols{position:absolute;left:47px;top:20px;width:610px;display:grid;grid-template-columns:1.5fr 1fr 1fr 1fr;gap:20px}
.footer-cols h6{color:var(--white);font-size:10px;font-weight:600;margin-bottom:8px}
.footer-cols p,.footer-cols li{font-size:7px;line-height:1.6}
.footer-cols ul{list-style:none}
.footer-cols .date{color:var(--pink);font-size:6.5px}
.social li{display:flex;align-items:center;gap:6px;margin-bottom:6px}
.social i{width:16px;height:16px;border-radius:50%;background:#4a4c55;display:block}
.bottom-bar{left:0;top:1166px;width:700px;height:34px;background:var(--darker);color:#8c8d95;font-size:7px;text-align:center;line-height:34px}
</style>
</head>
<body>

<header class="site-header abs">
  <div class="brand abs"><div class="brand-dot"></div><div class="brand-name">SOLVANE<br>WOMEN'S HEALTH</div></div>
  <div class="search abs">Search</div>
  <div class="contact abs" style="left:372px">
    <div class="ico"><svg width="11" height="11" viewBox="0 0 24 24"><path fill="#fff" d="M6.6 10.8a15 15 0 0 0 6.6 6.6l2.2-2.2c.3-.3.7-.4 1-.2 1.1.4 2.3.6 3.6.6.6 0 1 .4 1 1V20c0 .6-.4 1-1 1A17 17 0 0 1 3 4c0-.6.4-1 1-1h3.5c.6 0 1 .4 1 1 0 1.3.2 2.5.6 3.6.1.3 0 .7-.2 1z"/></svg></div>
    <div><strong>Call Us:</strong><span>1 (200) 555 0148</span></div>
  </div>
  <div class="contact abs" style="left:512px">
    <div class="ico"><svg width="11" height="11" viewBox="0 0 24 24"><path fill="#fff" d="M3 5h18v14H3z"/><path d="M3 5l9 7 9-7" stroke="#886aae" stroke-width="2" fill="none"/></svg></div>
    <div><strong>Email Us:</strong><span>hello@solvanehealth.com</span></div>
  </div>
</header>

<nav class="main-nav abs">
  <ul>
    <li class="active">HOME</li><li>ABOUT US</li><li>SERVICES</li><li>TIPS</li><li>E-BOOK</li><li>TESTIMONIALS</li><li>CONTACT US</li><li>FAQS</li>
  </ul>
</nav>

<section class="hero abs">
  <div class="hero-photo abs" role="img" aria-label="Photo of a smiling woman in a patterned blouse"></div>
  <div class="hero-copy abs">
    <div class="hero-kicker">SOLVANE</div>
    <div class="hero-title">Women's Health</div>
    <p class="hero-lead">Lorem Ipsum is simply dummy text of the printing and typesetting industry.</p>
    <span class="btn">Click here for more info</span>
  </div>
</section>

<section class="ebook-bar abs">
  <div class="ebook-copy abs">
    <h3>E-book download</h3>
    <p>Lorem Ipsum is simply dummy text of the printing and typesetting industry, Lorem Ipsum has been the standard dummy text.</p>
  </div>
  <span class="btn abs">FREE DOWNLOAD</span>
</section>

<main class="content abs">
  <section class="about">
    <h2 class="section-title">About Solvane Women's Health</h2>
    <p>Lorem Ipsum is simply dummy text of the printing and typesetting industry. Lorem Ipsum has been the industry's standard dummy text ever since the 1500s, when an unknown printer took a galley of type and scrambled it to make a type specimen book.</p>
    <p>It has survived not only five centuries, but also the leap into electronic typesetting, remaining essentially unchanged.</p>
    <span class="btn">View more info</span>
    <div class="about-photo" role="img" aria-label="Photo of a woman with arms open in a sunny field"></div>
  </section>

  <section class="tips">
    <h2 class="section-title">Tips &amp; Tricks</h2>
    <div class="tips-grid">
      <article class="tip"><div class="thumb t1" role="img" aria-label="Photo of a woman stretching"></div><h4>Lorem Ipsum is simply</h4><p>Lorem Ipsum is simply dummy text of the printing</p></article>
      <article class="tip"><div class="thumb t2" role="img" aria-label="Photo of a woman at a clinic visit"></div><h4>Lorem Ipsum is simply</h4><p>Lorem Ipsum is simply dummy text of the printing</p></article>
      <article class="tip"><div class="thumb t3" role="img" aria-label="Photo of a woman resting"></div><h4>Lorem Ipsum is simply</h4><p>Lorem Ipsum is simply dummy text of the printing</p></article>
      <article class="tip"><div class="thumb t4" role="img" aria-label="Photo of a smiling woman"></div><h4>Lorem Ipsum is simply</h4><p>Lorem Ipsum is simply dummy text of the printing</p></article>
      <article class="tip"><div class="thumb t5" role="img" aria-label="Photo of a woman doing yoga"></div><h4>Lorem Ipsum is simply</h4><p>Lorem Ipsum is simply dummy text of the printing</p></article>
      <article class="tip"><div class="thumb t6" role="img" aria-label="Photo of a woman by the sea"></div><h4>Lorem Ipsum is simply</h4><p>Lorem Ipsum is simply dummy text of the printing</p></article>
      <article class="tip"><div class="thumb t7" role="img" aria-label="Photo of a woman jumping outdoors"></div><h4>Lorem Ipsum is simply</h4><p>Lorem Ipsum is simply dummy text of the printing</p></article>
      <article class="tip"><div class="thumb t8" role="img" aria-label="Photo of a woman relaxing at home"></div><h4>Lorem Ipsum is simply</h4><p>Lorem Ipsum is simply dummy text of the printing</p></article>
    </div>
    <span class="btn">View more Tips</span>
  </section>
</main>

<aside class="sidebar abs">
  <div class="card">
    <div class="card-head">Newsletter signup</div>
    <div class="card-body">
      Get exclusive updates through your email id
      <div class="field">Enter your name</div>
      <div class="field">Enter your Email</div>
      <span class="btn">Subscribe now</span>
    </div>
  </div>
  <div class="card">
    <div class="story-photo" role="img" aria-label="Photo of a woman reading"></div>
    <div class="card-body">
      <h5>Top Stories</h5>
      Lorem Ipsum is simply dummy text of the printing and typesetting industry. Lorem Ipsum has been the standard dummy text ever since.
      <span class="btn">View more Stories</span>
    </div>
  </div>
  <div class="card testimonial">
    <div class="card-body">
      <h5>Testimonials</h5>
      <div class="avatar" role="img" aria-label="Portrait photo of a patient"></div>
      <div class="name">Dana Whitfield</div>
      <div class="role">Happy Mom</div>
      Lorem Ipsum is simply dummy text of the printing and typesetting industry, standard dummy text ever since the 1500s.
    </div>
  </div>
</aside>

<footer class="site-footer abs">
  <div class="footer-cols">
    <div>
      <h6>Latest News</h6>
      <p>Simply dummy text of the printing and typesetting.</p>
      <p class="date">Posted on 12 January 2024</p>
      <p>Lorem Ipsum is simply dummy text of the printing and typesetting industry. Lorem Ipsum has been the standard dummy text ever since the 1500s.</p>
    </div>
    <div>
      <h6>Welcome</h6>
      <ul><li>Home</li><li>About us</li><li>Services</li><li>Tips</li><li>E-Book</li><li>Testimonials</li><li>Contact us</li><li>FAQs</li></ul>
    </div>
    <div>
      <h6>Information</h6>
      <ul><li>Privacy Policy</li><li>Terms &amp; Conditions</li><li>Sitemap</li></ul>
    </div>
    <div>
      <h6>Follow Us</h6>
      <ul class="social"><li><i></i>Network one</li><li><i></i>Network two</li><li><i></i>Network three</li><li><i></i>Network four</li></ul>
    </div>
  </div>
</footer>
<div class="bottom-bar abs">© 2024 Solvane Women's Health. All rights reserved.</div>

</body>
</html>
```